WP website design (TOVI)

We need a wordpress design that will incorporate a professional color scheme with company logo in a clean layout. The design needs to consider that this will be developed on a responsive theme. Colors are undetermined - those that will complement the logo.
Client mentions liking plinmerbid.com for the layout and use of color. Possible but not necessary to have large slideshow element.

Industry/Entity Type

It Company

Font styles to use
Sans Serif

Colors

Designer to choose colors to be used in the design.

Requirements
Must have
• - Navigation: 1)Home 2) Auctions 3) Services 4) About Us 5) FAQs 6) References 7) Contact Us

Site will have slideshow, please use high-end stock real estate image initially. Header will have logo. Social icons (Facebook, Twitter, Youtube)

Widgets Include: Email signup form, Featured Auctions, Featured Video widget.

Footer will have contact info (below), site navigation, smaller company logo, affiliation logos (attached).

TOVI Auction Group
4275 Birch Vale Lane
Marlowe, KY 40617
1-800-419-BIDS (2437)
Ph. (270) 386-9041
Fx. (270) 386-1158
Nice to have
• - Site will have drop-down menus - please indicate the styling, for instance the dropdown menus 1) Live 2) Online 3) Past - under the 'Auctions' link

```html
<!DOCTYPE html>
<html lang="en">
<head>
<meta charset="utf-8">
<title>TOVI Auction Group</title>
<link href="https://fonts.googleapis.com/css2?family=Arimo:wght@400;700&family=Libre+Baskerville&family=PT+Sans:wght@400;700&display=swap" rel="stylesheet">
<style>
:root{
  --red:#d4000f;
  --red-dark:#b0000b;
  --ink:#2e2e2e;
  --brown:#7a3d0a;
  --gold:#8a5a12;
  --footer:#3a3a3a;
  --grey:#4a4a4a;
  --white:#ffffff;
}
*{margin:0;padding:0;box-sizing:border-box}
html,body{width:954px;height:1200px;overflow:hidden;background:var(--white)}
body{position:relative;font-family:'Arimo',sans-serif;color:var(--ink)}
.abs{position:absolute}
.brand{left:80px;top:36px;font-family:'PT Sans',sans-serif;font-weight:700;font-size:22px;color:var(--red);display:flex;align-items:center;gap:8px;line-height:1}
.brand .dot{width:22px;height:22px;border-radius:50%;background:var(--red)}
.follow{left:666px;top:42px;font-family:'PT Sans',sans-serif;font-size:19px;color:#333}
.social{top:38px;width:28px;height:28px;border-radius:50%}
.nav{left:0;top:98px;width:954px;height:32px;background:var(--red);border-bottom:2px solid var(--white)}
.nav a{position:absolute;top:8px;font-family:'PT Sans',sans-serif;font-size:13px;color:var(--white);text-decoration:none}
.nav .sep{position:absolute;top:0;width:1px;height:30px;background:var(--red-dark)}
.nav .caret{position:absolute;left:180px;top:26px;width:0;height:0;border-left:5px solid transparent;border-right:5px solid transparent;border-bottom:5px solid var(--white)}
.hero{left:0;top:132px;width:954px;height:418px;background:linear-gradient(90deg,#2b2f36 0%,#6a6c72 30%,#c9a69a 50%,#d9c7c0 70%,#3a3e45 100%)}
.hero .roof{position:absolute;left:300px;top:0;width:300px;height:200px;background:linear-gradient(160deg,#e0131b,#b50d12);opacity:.85}
.dropdown{left:109px;top:140px;width:162px;height:118px;background:#cfcfcf;border-radius:2px}
.dropdown div{position:absolute;left:6px;width:147px;height:23px;border-radius:3px;font-family:'PT Sans',sans-serif;font-size:11px;color:var(--white);padding:5px 0 0 20px;background:#3c3c3c}
.dropdown div::before{content:"";position:absolute;left:10px;top:8px;border-top:3px solid transparent;border-bottom:3px solid transparent;border-left:4px solid var(--white)}
.dropdown .active{background:var(--red)}
.serif{font-family:'Libre Baskerville',serif;font-weight:400}
.welcome{left:80px;top:592px;font-size:19px;color:var(--ink)}
.welcome span,.h2 {color:var(--red)}
.lead{left:83px;top:634px;width:490px;font-size:11px;font-weight:700;line-height:16px;color:var(--brown)}
.body-text{left:83px;top:682px;width:485px;font-size:9.5px;line-height:16px;color:#333}
.divider{left:600px;top:580px;height:465px;border-left:1px dotted #999}
.signup{left:633px;top:590px;width:240px;height:199px;background:linear-gradient(#d4000f,#c4000c);border-radius:4px;color:var(--white)}
.signup h3{position:absolute;left:19px;top:13px;font-size:17px;letter-spacing:.5px}
.signup p{position:absolute;left:21px;top:40px;width:205px;font-family:'PT Sans',sans-serif;font-size:10px;line-height:13px}
.signup .field{position:absolute;left:21px;width:195px;height:23px;background:var(--white);border:1px solid #ccc;font-size:10px;color:#888;padding:5px 0 0 6px}
.signup .btn{position:absolute;left:21px;top:160px;width:108px;height:27px;border-radius:14px;background:linear-gradient(#fff,#ddd);border:2px solid #555;font-family:'PT Sans',sans-serif;font-weight:700;font-size:11px;color:#222;text-align:center;padding-top:5px}
.h2{font-size:19px}
.thumb{left:79px;top:868px;width:98px;height:65px;border:1px solid #ddd;padding:3px;background:var(--white)}
.thumb div{width:100%;height:100%;background:linear-gradient(#7fa9d6 0%,#b9cde0 40%,#8a7a5c 60%,#6d8a4a 100%)}
.a-title{left:192px;top:869px;font-size:11px;letter-spacing:.6px;color:#222}
.a-type{left:192px;top:887px;font-family:'PT Sans',sans-serif;font-size:11px;color:var(--gold)}
.a-meta{left:192px;font-size:9.5px;color:#222}
.a-meta b{margin-right:4px}
.a-btn{left:82px;width:78px;height:23px;border-radius:3px;font-family:'PT Sans',sans-serif;font-size:10.5px;color:var(--white);display:flex;align-items:center;justify-content:center;gap:6px}
.a-text{left:192px;top:949px;width:316px;font-size:9.5px;line-height:15px;text-align:justify;color:#333}
.video{left:632px;top:872px;width:242px;height:143px;background:#111;padding:2px}
.video .screen{width:100%;height:121px;background:linear-gradient(90deg,#c9a27a,#6ea0d8 60%,#2a6fc4)}
.video .play{position:absolute;left:95px;top:48px;width:54px;height:38px;background:rgba(20,20,20,.7)}
.video .bar{position:absolute;left:2px;bottom:2px;width:238px;height:18px;background:#222}
.footer{left:0;top:1051px;width:954px;height:123px;background:var(--footer)}
.address{left:85px;top:1070px;font-family:'PT Sans',sans-serif;font-size:11px;line-height:16px;color:var(--white)}
.fnav a{position:absolute;top:1078px;font-family:'PT Sans',sans-serif;font-size:11px;color:var(--white);text-decoration:none}
.badge{top:1110px;height:48px;background:#cfcfcf;border-radius:6px}
.flogo{left:513px;top:1124px;font-family:'PT Sans',sans-serif;font-weight:700;font-size:13px;color:var(--white)}
.copy{left:0;top:1174px;width:954px;height:26px;background:var(--red);color:var(--white);font-size:9.5px;text-align:center;padding-top:7px}
</style>
</head>
<body>
<div class="abs brand"><span class="dot"></span>TOVI Auction Group</div>
<div class="abs follow">Follow Us:</div>
<div class="abs social" style="left:765px;background:#3b5998"></div>
<div class="abs social" style="left:803px;background:#1da1f2"></div>
<div class="abs social" style="left:842px;background:#d9312a"></div>

<nav class="abs nav">
  <a style="left:81px">Home</a><span class="sep" style="left:140px"></span>
  <a style="left:162px">Auctions</a><span class="sep" style="left:234px"></span>
  <a style="left:257px">Services</a><span class="sep" style="left:327px"></span>
  <a style="left:349px">About Us</a><span class="sep" style="left:422px"></span>
  <a style="left:446px">FAQs</a><span class="sep" style="left:499px"></span>
  <a style="left:522px">References</a><span class="sep" style="left:603px"></span>
  <a style="left:628px">Contact Us</a>
  <span class="caret"></span>
</nav>

<div class="abs hero" role="img" aria-label="Slideshow photo: hand holding a small model house with a red roof"><div class="roof"></div></div>

<div class="abs dropdown">
  <div class="active" style="top:17px">Live</div>
  <div style="top:47px">Online</div>
  <div style="top:78px">Past</div>
</div>

<h1 class="abs welcome serif"><span>WELCOME</span> TOVI AUCTION GROUP</h1>
<p class="abs lead">Lorem Ipsum is that it has a more-or-less normal distribution of letters, as opposed to using Content here, content here', making it look like readable English.</p>
<p class="abs body-text">Many desktop publishing packages and web page editors now&nbsp; Lorem Ipsum as their default model text, and a search for 'lorem ipsum' will uncover many web sites still in their infancy the years. by accident, sometimes on purpose (injected humour and the likelike readable English. Many desktop publishing packages and web page editors now use Lorem Ipsum as their default model text, and a search for 'lorem ipsum' will uncover many web sites still in their infancy...</p>

<div class="abs divider"></div>

<form class="abs signup">
  <h3 class="serif">EMAIL SIGNUP FORM</h3>
  <p>Lorem ipsum dolor sit amet, consectetuer adipiscing elit. Nam</p>
  <div class="field" style="top:79px">Your Name</div>
  <div class="field" style="top:120px">Email Address</div>
  <div class="btn">Subscribe Now</div>
</form>

<h2 class="abs h2 serif" style="left:81px;top:830px">FEATURED AUCTIONS</h2>
<div class="abs thumb"><div role="img" aria-label="Photo of a two-storey family house"></div></div>
<div class="abs a-title">SHOP EQUIPMENT/TOOLS * PORK PROCESSING ITEMS</div>
<div class="abs a-type">LIVE ON-SITE AUCTION</div>
<div class="abs a-meta" style="top:905px"><b>Begins:</b>Saturday, March 16, 2013 at 10:00 AM EDT</div>
<div class="abs a-meta" style="top:921px"><b>Location:</b>2918 Harlan Road Fairdale, KY 40118</div>
<div class="abs a-btn" style="top:950px;background:var(--red)">
  <svg width="18" height="10" viewBox="0 0 18 10"><rect x="0" y="0" width="7" height="10" fill="#fff"/><rect x="9" y="0" width="9" height="2" fill="#fff"/><rect x="9" y="4" width="9" height="2" fill="#fff"/><rect x="9" y="8" width="9" height="2" fill="#fff"/></svg>Details</div>
<div class="abs a-btn" style="top:983px;background:#2b2b2b">
  <svg width="14" height="12" viewBox="0 0 14 12"><rect x="1" y="1" width="12" height="10" fill="none" stroke="#fff" stroke-width="1.5"/><path d="M2 10l4-4 3 3 2-2 2 3z" fill="#fff"/></svg>Gallery</div>
<p class="abs a-text">Lorem ipsum dolor sit amet, consectetur adipiscing elit, sed do eiusmod tempor incididunt ut labore et dolore magna aliqua. Ut enim pariatur. Excepteur sint occaecat cupidatat non proident, sunt in culpa qui officia deserunt mollit anim id est laborum.</p>

<h2 class="abs h2 serif" style="left:632px;top:834px">FEATURED VIDEO</h2>
<div class="abs video">
  <div class="screen" role="img" aria-label="Video still: hand holding house keys in front of a home"></div>
  <div class="play"><svg width="54" height="38" viewBox="0 0 54 38"><path d="M22 9l14 10-14 10z" fill="#ddd"/></svg></div>
  <div class="bar"><svg width="238" height="18" viewBox="0 0 238 18"><path d="M12 5l6 4-6 4z" fill="#fff"/><text x="26" y="13" font-size="8" fill="#fff" font-family="Arimo,sans-serif">00:00</text><rect x="54" y="8" width="124" height="3" fill="#777"/><text x="188" y="13" font-size="8" fill="#fff" font-family="Arimo,sans-serif">00:00</text><rect x="226" y="5" width="8" height="8" fill="none" stroke="#fff"/></svg></div>
</div>

<footer class="abs footer"></footer>
<address class="abs address" style="font-style:normal">TOVI Auction Group<br>4275 Birch Vale Lane<br>Marlowe, KY 40617<br>1-800-419-BIDS (2437)<br>Ph. (270) 386-9041<br>Fx. (270) 386-1158</address>
<nav class="fnav">
  <a style="left:365px">Home</a><a style="left:431px">Auctions</a><a style="left:510px">Services</a><a style="left:586px">About Us</a><a style="left:666px">FAQs</a><a style="left:727px">References</a><a style="left:815px">Contact Us</a>
</nav>
<div class="abs flogo">TOVI</div>
<div class="abs badge" style="left:606px;width:40px"></div>
<div class="abs badge" style="left:659px;width:83px;border-radius:24px"></div>
<div class="abs badge" style="left:751px;width:50px"></div>
<div class="abs badge" style="left:815px;width:46px"></div>
<div class="abs copy">Copyright (C) Tovi auction group. 2013.&nbsp; All Rights Reserved</div>
</body>
</html>
```